We need a complete design for our construction company KELMO CONSTRUCTION based in Auckland New Zealand, we need a logo, website, business card, vehicle design etc..
We are a mid to high-end construction company who work mostly on residential projects and some commercial.

What we want to see in the design;
Professional,
Architectural,
Simple,
Alternative,

We want the design to communicate professionalism, high quality wormanship and and quality service.

Target Market(s)

People looking for a quality building/ construction company

Industry/Entity Type

Construction Company

Contact Information for Business Card

KELMO CONSTRUCTION.co.nz
Teo Vrankel
teo@kelmoconstruction.example.nz
021 5873 406

Logo Text

KELMO CONSTRUCTION

Number of Pages Required

5+ page

Font styles to use
Sans Serif

Colors

Designer to choose colors to be used in the design.

Requirements
Must have
• Must appear high end, professional, quality, be simple, easy to use, give security to potential clients
Nice to have
• high-quality photos of our recent projects
• about us page
• blog page
• contact us page
• high quality content
Should not have
• should not be hard to use and have too much going on.

```html
<!DOCTYPE html>
<html lang="en">
<head>
<meta charset="utf-8">
<title>KELMO Construction</title>
<link rel="stylesheet" href="https://fonts.googleapis.com/css2?family=Montserrat:wght@400;500;600;700&family=Roboto:wght@400;500&display=swap">
<style>
:root{
  --blue:#1a6fe3;
  --orange:#f2561d;
  --white:#ffffff;
  --ink:#222222;
  --muted:#666666;
  --footer:#1f1f1f;
  --line:#cfcfcf;
  --frame:rgba(255,255,255,.75);
}
*{margin:0;padding:0;box-sizing:border-box}
html,body{width:1200px;height:2597px;overflow:hidden}
body{position:relative;background:var(--white);font-family:"Montserrat",sans-serif;color:var(--ink)}
.abs{position:absolute}

/* hero */
.hero{left:0;top:0;width:1200px;height:655px;
  background:
    radial-gradient(ellipse 260px 330px at 230px 380px,#e0641f 0%,rgba(224,100,31,0) 100%),
    radial-gradient(ellipse 240px 320px at 640px 420px,#2c2a2a 0%,rgba(44,42,42,0) 100%),
    radial-gradient(ellipse 260px 330px at 920px 380px,#e36a22 0%,rgba(227,106,34,0) 100%),
    linear-gradient(180deg,#6d6a66 0%,#8c8479 40%,#5d5853 100%)}
.hero-shade{left:0;top:0;width:1200px;height:655px;background:rgba(0,0,0,.22)}
.logo{left:120px;top:31px;font-size:28px;font-weight:600;color:var(--white);white-space:nowrap}
.nav a{position:absolute;top:38px;font-size:16px;font-weight:500;color:var(--white);text-decoration:none;white-space:nowrap}
.nav-mark{left:502px;top:0;width:56px;height:5px;background:var(--orange)}
.hero-title{left:0;width:1200px;top:280px;text-align:center;color:var(--white);font-weight:700;font-size:46px;line-height:1}
.hero-sub{left:0;width:1200px;top:335px;text-align:center;color:var(--white);font-weight:600;font-size:33px;line-height:1}
.btn-orange{left:520px;top:388px;width:157px;height:42px;background:var(--orange);color:var(--white);font-size:15px;font-weight:600;display:flex;align-items:center;justify-content:center}
.arrow{width:52px;height:52px;top:301px}

/* welcome */
.band{left:0;top:655px;width:1200px;height:1293px}
.welcome-title{left:0;width:1200px;top:714px;text-align:center;font-size:31px;font-weight:500;color:var(--white)}
.welcome-text{left:215px;width:770px;top:772px;text-align:center;font-size:14.5px;line-height:25px;color:#dbe7fb}
.hex{width:216px;height:190px;top:940px}
.service-title{font-size:20px;font-weight:700;line-height:21px;color:var(--white)}
.service-text{width:218px;font-size:13px;line-height:21px;color:#dbe7fb}
.btn-outline{width:128px;height:33px;border:2px solid var(--white);color:var(--white);font-size:12.5px;font-weight:600;display:flex;align-items:center;justify-content:center}

/* projects */
.section-title{left:0;width:1200px;top:1242px;text-align:center;font-size:31px;font-weight:600;color:var(--white)}
.photo{border:2px solid var(--frame)}

/* blogs */
.blogs-title{left:130px;top:1990px;font-size:28px;font-weight:500;color:var(--ink)}
.card{top:2051px;width:302px;height:344px;border:2px solid var(--line);background:var(--white)}
.card-photo{left:0;top:0;width:298px;height:195px}
.date{left:0;top:133px;width:64px;height:62px;background:var(--orange);color:var(--white);text-align:center}
.date b{display:block;font-family:"Roboto",sans-serif;font-weight:500;font-size:27px;line-height:30px;margin-top:6px}
.date span{display:block;font-size:15px;line-height:18px}
.card-title{left:23px;top:213px;font-family:"Roboto",sans-serif;font-size:19px;font-weight:400;color:var(--ink)}
.card-text{left:23px;top:245px;width:262px;font-family:"Roboto",sans-serif;font-size:12.5px;line-height:18px;color:var(--muted)}
.card-link{left:23px;top:305px;font-family:"Roboto",sans-serif;font-size:12px;font-weight:500;color:var(--blue)}

/* footer */
.footer{left:0;top:2447px;width:1200px;height:150px;background:var(--footer)}
.foot-nav a{position:absolute;top:2497px;font-size:14px;font-weight:500;color:var(--white);text-decoration:none}
.copyright{left:120px;top:2536px;font-family:"Roboto",sans-serif;font-size:13px;color:#bdbdbd}
.social{top:2493px;width:40px;height:40px;border:2px solid var(--white);border-radius:50%;display:flex;align-items:center;justify-content:center;font-size:9px;font-weight:600;color:var(--white);text-decoration:none}
</style>
</head>
<body>

<!-- hero -->
<div class="abs hero" role="img" aria-label="Three construction workers in hard hats and high-visibility vests reviewing plans on site"></div>
<div class="abs hero-shade"></div>
<div class="abs nav-mark"></div>
<div class="abs logo">KELMO Construction</div>
<nav class="nav">
  <a style="left:507px" href="#">HOME</a>
  <a style="left:607px" href="#">ABOUT US</a>
  <a style="left:738px" href="#">PROJECTS</a>
  <a style="left:868px" href="#">BLOG</a>
  <a style="left:962px" href="#">CONTACT US</a>
</nav>
<h1 class="abs hero-title">HIGH-END RESIDENTIAL AND</h1>
<div class="abs hero-sub">COMMERCIAL CONSTRUCTION</div>
<div class="abs btn-orange">READ MORE</div>
<svg class="abs arrow" style="left:80px" viewBox="0 0 52 52"><circle cx="26" cy="26" r="24" fill="none" stroke="#fff" stroke-width="2"/><path d="M30 16 L20 26 L30 36" fill="none" stroke="#fff" stroke-width="3"/></svg>
<svg class="abs arrow" style="left:1053px" viewBox="0 0 52 52"><circle cx="26" cy="26" r="24" fill="none" stroke="#fff" stroke-width="2"/><path d="M22 16 L32 26 L22 36" fill="none" stroke="#fff" stroke-width="3"/></svg>

<!-- blue / grey band -->
<svg class="abs band" viewBox="0 0 1200 1293" preserveAspectRatio="none">
  <defs>
    <linearGradient id="greyFade" x1="0" y1="0" x2="0" y2="1">
      <stop offset="0" stop-color="#cfcfcf"/>
      <stop offset="1" stop-color="#e4e4e4"/>
    </linearGradient>
  </defs>
  <rect x="0" y="0" width="1200" height="1293" fill="url(#greyFade)"/>
  <polygon points="0,0 1200,0 1200,644 0,790" fill="var(--blue)"/>
</svg>

<h2 class="abs welcome-title">WELCOME TO KELMO</h2>
<p class="abs welcome-text">Praesent elementum elit at tellus nec ultricies sit amet porttitor mattis enim In massa libero interdum nec interdum vel blandit sed nulla In ullamcorper est eget tempor cursus neque mi consectetuer mi a ultricies massa est sed nisl Class aptent taciti sociosqu ad litora torquent per conubia</p>

<!-- services -->
<svg class="abs hex" style="left:121px" viewBox="0 0 216 190" role="img" aria-label="Residential house under construction with brick walls and roof framing">
  <defs><linearGradient id="hexRes" x1="0" y1="0" x2="0" y2="1"><stop offset="0" stop-color="#b3c7dc"/><stop offset=".45" stop-color="#a6a29c"/><stop offset=".6" stop-color="#9a5640"/><stop offset="1" stop-color="#7a4636"/></linearGradient></defs>
  <polygon points="54,3 162,3 213,95 162,187 54,187 3,95" fill="url(#hexRes)" stroke="#fff" stroke-width="4"/>
</svg>
<div class="abs service-title" style="left:362px;top:942px">RESIDENTIAL<br>CONSTRUCTION</div>
<p class="abs service-text" style="left:362px;top:998px">Praesent elementum elit at tellus nec ultricies sit amet porttitor mattis enim In massa libero interdum nec interdum vel blandit sed nulla In ullamcorper</p>
<div class="abs btn-outline" style="left:364px;top:1115px">READ MORE</div>

<svg class="abs hex" style="left:625px" viewBox="0 0 216 190" role="img" aria-label="Commercial tower under construction with crane">
  <defs><linearGradient id="hexCom" x1="0" y1="0" x2="0" y2="1"><stop offset="0" stop-color="#8fb4dc"/><stop offset=".5" stop-color="#6f7f92"/><stop offset=".8" stop-color="#6a4a3a"/><stop offset="1" stop-color="#3d3a38"/></linearGradient></defs>
  <polygon points="54,3 162,3 213,95 162,187 54,187 3,95" fill="url(#hexCom)" stroke="#fff" stroke-width="4"/>
</svg>
<div class="abs service-title" style="left:865px;top:942px">COMMERCIAL<br>CONSTRUCTION</div>
<p class="abs service-text" style="left:865px;top:998px">Praesent elementum elit at tellus nec ultricies sit amet porttitor mattis enim In massa libero interdum nec interdum vel blandit sed nulla In ullamcorper</p>
<div class="abs btn-outline" style="left:867px;top:1115px">READ MORE</div>

<!-- recent projects -->
<h2 class="abs section-title">RECENT PROJECTS</h2>
<div class="abs photo" style="left:119px;top:1316px;width:629px;height:347px;background:linear-gradient(180deg,#a9c9ec 0%,#d6e2ee 40%,#c9ccd0 65%,#5f6670 100%)" role="img" aria-label="Modern white apartment building with balconies against blue sky"></div>
<div class="abs photo" style="left:767px;top:1316px;width:305px;height:170px;background:linear-gradient(180deg,#d4d4d4 0%,#a9bdd2 45%,#3f6fa6 75%,#c4502e 100%)" role="img" aria-label="Close view of a glass and panel commercial facade"></div>
<div class="abs photo" style="left:767px;top:1498px;width:305px;height:172px;background:linear-gradient(180deg,#5a95d8 0%,#c9a67a 45%,#8a6a4c 75%,#46622f 100%)" role="img" aria-label="Apartment blocks at golden hour with trees"></div>
<div class="abs photo" style="left:119px;top:1680px;width:305px;height:208px;background:linear-gradient(180deg,#3a4f86 0%,#9aa4c0 40%,#e4e2de 55%,#2c3b66 100%)" role="img" aria-label="Modern white residence with pool at dusk"></div>
<div class="abs photo" style="left:447px;top:1680px;width:305px;height:208px;background:linear-gradient(180deg,#1f3a6a 0%,#4a5a7a 40%,#a36b3c 62%,#3d5a2a 100%)" role="img" aria-label="Brick family home lit up at evening"></div>
<div class="abs photo" style="left:767px;top:1680px;width:305px;height:208px;background:linear-gradient(180deg,#6f8fb8 0%,#8ea2b8 45%,#d89a4f 78%,#3a3a3a 100%)" role="img" aria-label="Glass office building at sunset"></div>

<!-- blogs -->
<h2 class="abs blogs-title">OUR BLOGS</h2>

<article class="abs card" style="left:116px">
  <div class="abs card-photo" style="background:linear-gradient(180deg,#9cc3e8 0%,#8a9aa8 45%,#b07a3e 75%,#6a5a48 100%)" role="img" aria-label="Worker on a building site with timber framing and steel beams"></div>
  <div class="abs date"><b>20</b><span>FEB</span></div>
  <h3 class="abs card-title">Your Blog Title here</h3>
  <p class="abs card-text">netus et malesuada fames ac turpis egestas Cras id elit Integer quis urna Ut ante enim dapibus malesuada fringilla eu cond</p>
  <div class="abs card-link">READ MORE</div>
</article>

<article class="abs card" style="left:439px">
  <div class="abs card-photo" style="background:linear-gradient(180deg,#5c5a58 0%,#7d7268 45%,#3a4f7a 70%,#4a4540 100%)" role="img" aria-label="Workers tying steel reinforcement bars"></div>
  <div class="abs date"><b>15</b><span>FEB</span></div>
  <h3 class="abs card-title">Your Blog Title here</h3>
  <p class="abs card-text">netus et malesuada fames ac turpis egestas Cras id elit Integer quis urna Ut ante enim dapibus malesuada fringilla eu cond</p>
  <div class="abs card-link">READ MORE</div>
</article>

<article class="abs card" style="left:762px">
  <div class="abs card-photo" style="background:linear-gradient(180deg,#8a3a3a 0%,#c45a3a 40%,#f2a04a 65%,#2a1a14 100%)" role="img" aria-label="Silhouettes of builders against a sunset"></div>
  <div class="abs date"><b>09</b><span>FEB</span></div>
  <h3 class="abs card-title">Your Blog Title here</h3>
  <p class="abs card-text">netus et malesuada fames ac turpis egestas Cras id elit Integer quis urna Ut ante enim dapibus malesuada fringilla eu cond</p>
  <div class="abs card-link">READ MORE</div>
</article>

<!-- footer -->
<footer class="abs footer"></footer>
<nav class="foot-nav">
  <a style="left:120px" href="#">HOME</a>
  <a style="left:207px" href="#">ABOUT US</a>
  <a style="left:324px" href="#">PROJECTS</a>
  <a style="left:440px" href="#">BLOG</a>
  <a style="left:523px" href="#">CONTACT US</a>
</nav>
<div class="abs copyright">© 2018 Company Name &nbsp;All right reserved &nbsp;Terms of Use</div>
<a class="abs social" style="left:933px" href="#">Pebl</a>
<a class="abs social" style="left:980px" href="#">Sona</a>
<a class="abs social" style="left:1026px" href="#">Vexa</a>

</body>
</html>
```